Maple Harbour Website

We are starting a marketing company and to do that we need a website! We want a website that will inspire and persuade to bring out the awesomeness in our clients.
What we want to see:
- Inspirational and persuasive imagery that relate to Branding.
- No cliche images eg. business man, suits and hand shakes
- We want to transform and educate our clients.
- We want to show them the path and would like our website to really act as a guide that guides them step by step through our process.
- We want the portray that we are an investment but not have a pretentious way to it. We put our heart into every project and that is how we treat our clients.
-When you submit your design please include what platform you have created for. Preference would be Wordpress or Joobla.

We have included the psd file for the wire frame, logo files, font files, site map and a link to a video we create to give you more information on what we would like to see. http://clipvault-example.com/t/qk82LmPzr

Feel free to make small modification to the logos if you think it will improve it. Your creativity and advice is most welcome.
Updates

One thing we forgot. We would like to have our contact information near the top of the website as well as at the bottom.  Here is out contact info:

Email: info@mapleharbour.ca
Phone: 403-555-0142

Reason: As we are new with the platform and that we want to optimize our results, we decided to extend the deadline by 15 days. Thanks!

Target Market(s)

28-60, Male and Female, Oil field, Local Businesses, Dentists, Chiropractors, Hair salon, Construction/Renovation, Events etc

Industry/Entity Type

Investment

Requirements
Must have
• - 4 Inspirational and persuasive Imagery for the top portion of the website
- Must have a feel as if your not on a website an example of this is linked below.
http://www.pixelforum-sample.com/design/472093/web-design-by-helen-dawes
Nice to have
• - Creative advice from you.
- Creative buttons for Get Free Quote and Subscribe buttons. Something out of the box that draws peoples attention. eg. a 'B' button. Just and example but still something related to branding.
Should not have
• No Cliches

```html
<!DOCTYPE html>
<html lang="en">
<head>
<meta charset="utf-8">
<title>Maple Harbour</title>
<link href="https://fonts.googleapis.com/css2?family=Baloo+2:wght@700&family=Ubuntu:wght@700&family=Arimo:wght@400;700&display=swap" rel="stylesheet">
<style>
:root{
  --page-bg:#e8e8e8;
  --white:#ffffff;
  --green:#8cc63f;
  --green-dark:#5e9a1e;
  --green-band-top:#9fd43a;
  --green-band-bottom:#5f9b22;
  --nav-dark:#3a3a3a;
  --nav-dark2:#555555;
  --text:#2a2a2a;
  --footer:#2b2b2b;
  --logo-grey:#6d6d6d;
}
*{margin:0;padding:0;box-sizing:border-box}
html,body{width:1200px;height:794px;overflow:hidden}
body{background:var(--page-bg);font-family:"Arimo",Arial,sans-serif;position:relative}
.site{position:absolute;left:120px;top:0;width:960px;height:794px;background:var(--white)}
.sidebar{position:absolute;left:0;top:0;width:203px;height:320px;background:linear-gradient(180deg,#f4f5f7 0%,#d9dde6 60%,#b7bcc8 100%)}
.logo{position:absolute;left:8px;top:14px;display:flex;align-items:center;gap:8px}
.logo-mark{width:26px;height:26px;border-radius:50%;background:var(--logo-grey)}
.logo-name{font-family:"Arimo",Arial,sans-serif;font-weight:700;font-size:22px;color:var(--logo-grey);line-height:1.05;letter-spacing:.5px}
.tagline{position:absolute;left:32px;top:70px;font-size:12px;font-style:italic;color:#444}
.main-nav{position:absolute;left:1px;top:109px;list-style:none}
.main-nav li{height:34px;margin-bottom:6px;width:130px;background:linear-gradient(180deg,var(--nav-dark2),var(--nav-dark));display:flex;align-items:center;padding-left:10px;gap:9px;font-family:"Ubuntu",sans-serif;font-weight:700;font-size:13px;color:var(--white);letter-spacing:.5px}
.main-nav li.active{width:170px;background:linear-gradient(180deg,#a6d83e,#7bb52a)}
.main-nav svg{width:15px;height:15px}
.hero{position:absolute;left:203px;top:0;width:757px;height:320px;background:linear-gradient(135deg,#6f7e5a 0%,#a7b58a 35%,#8ea36b 60%,#c3a56a 85%,#d9c9a0 100%)}
.steps{position:absolute;left:72px;top:15px;width:665px;height:36px;background:rgba(120,120,120,.45);display:flex;justify-content:space-around;align-items:center;font-family:"Ubuntu",sans-serif;font-weight:700;font-size:16px;color:rgba(255,255,255,.35);letter-spacing:.5px}
.steps .current{color:var(--white)}
.band{position:absolute;left:108px;top:320px;width:984px;height:40px;background:linear-gradient(180deg,var(--green-band-top),var(--green-band-bottom))}
.band-ear{position:absolute;top:303px;width:14px;height:18px;background:var(--green-band-top)}
.band-ear.left{left:108px;border-top-left-radius:10px}
.band-ear.right{left:1078px;border-top-right-radius:10px}
.social{position:absolute;left:36px;top:5px;display:flex;gap:7px}
.social span{width:29px;height:29px;border-radius:50%;background:#f1f1f1;border:2px solid #dcdcdc}
.newsletter{position:absolute;left:266px;top:7px;font-family:"Ubuntu",sans-serif;font-weight:700;font-size:17px;color:var(--white)}
.btn-subscribe{position:absolute;left:737px;top:6px;width:85px;height:29px;border-radius:15px;background:linear-gradient(180deg,#555,#222);color:var(--white);font-family:"Ubuntu",sans-serif;font-weight:700;font-size:13px;display:flex;align-items:center;justify-content:center}
.btn-quote{position:absolute;left:833px;top:6px;width:137px;height:29px;border-radius:15px;background:var(--white);color:#222;font-family:"Ubuntu",sans-serif;font-weight:700;font-size:13px;display:flex;align-items:center;justify-content:center}
.content{position:absolute;left:150px;top:362px;width:660px;height:318px;background:linear-gradient(180deg,#fbfbfb 0%,#f0f0f0 100%)}
.content h1{height:62px;border-bottom:1px solid #e2e2e2;text-align:center;font-family:"Baloo 2",sans-serif;font-weight:700;font-size:30px;color:var(--green-dark);line-height:70px;background:linear-gradient(180deg,#ffffff,#f6f6f6)}
.content p{margin:14px 10px 0;font-size:13px;line-height:20px;color:var(--text);text-align:justify}
.content p + p{margin-top:20px}
.footer{position:absolute;left:0;top:700px;width:960px;height:94px;background:var(--footer);color:var(--white)}
.footer-nav{position:absolute;left:192px;top:23px;display:flex;list-style:none;font-size:12px;font-weight:700}
.footer-nav li + li::before{content:"|";margin:0 18px}
.copyright{position:absolute;left:351px;top:48px;font-size:11px;letter-spacing:.3px}
</style>
</head>
<body>
<div class="site">
  <aside class="sidebar">
    <div class="logo"><span class="logo-mark"></span><span class="logo-name">MAPLE<br>HARBOUR</span></div>
    <div class="tagline">Because You´re Awesome!</div>
    <ul class="main-nav">
      <li class="active"><svg viewBox="0 0 16 16"><circle cx="8" cy="8" r="7.5" fill="#222"/><path d="M6 4.5 11 8 6 11.5z" fill="#fff"/></svg>STRATEGY</li>
      <li><svg viewBox="0 0 16 16"><circle cx="8" cy="8" r="7.5" fill="#fff"/><path d="M6 4.5 11 8 6 11.5z" fill="#333"/></svg>PORTFOLIO</li>
      <li><svg viewBox="0 0 16 16"><circle cx="8" cy="8" r="7.5" fill="#fff"/><path d="M6 4.5 11 8 6 11.5z" fill="#333"/></svg>ABOUT US</li>
      <li><svg viewBox="0 0 16 16"><circle cx="8" cy="8" r="7.5" fill="#fff"/><path d="M6 4.5 11 8 6 11.5z" fill="#333"/></svg>CONTACT US</li>
      <li><svg viewBox="0 0 16 16"><circle cx="8" cy="8" r="7.5" fill="#fff"/><path d="M6 4.5 11 8 6 11.5z" fill="#333"/></svg>BLOG</li>
    </ul>
  </aside>
  <div class="hero" role="img" aria-label="Photo of a boy drawing a large face on a fogged-up window">
    <div class="steps"><span>MAPLE HARBOUR</span><span class="current">BE FOUND</span><span>CONNECT</span><span>GET GROWING</span></div>
  </div>
  <main class="content">
    <h1>Welcome to Maple Harbour</h1>
    <p><b>Lorem Ipsum is simply dummy text of the printing and typesetting industry. Lorem Ipsum has been the industry's standard dummy text ever since the 1500s,</b> when an unknown printer took a galley of type and scrambled it to make a type specimen book. It has survived not only five centuries, but also the leap into electronic typesetting, remaining essentially unchanged. Contrary to popular belief, Lorem Ipsum is not simply random text. It has roots in a piece of classical Latin literature from 45 BC, making it over 2000 years old. Daniel Whitcombe,</p>
    <p><b>It was popularised in the 1960s with the release of Lettrafix sheets containing</b> Lorem Ipsum passages, and more recently with desktop publishing software like Folio PageSetter including versions of Lorem Ipsum.Contrary to popular belief, Lorem Ipsum is not simply random text. It has roots in a piece of classical Latin literature from 45 BC, making it over 2000 years old. Daniel Whitcombe,</p>
  </main>
  <footer class="footer">
    <ul class="footer-nav"><li>Site Map</li><li>Strategy</li><li>Portfolio</li><li>About Us</li><li>Contact Us</li><li>Blog</li></ul>
    <div class="copyright">©MAPLE HARBOUR INC. 2013</div>
  </footer>
</div>
<div class="band-ear left"></div>
<div class="band-ear right"></div>
<div class="band">
  <div class="social"><span></span><span></span><span></span><span></span></div>
  <div class="newsletter">Get Tips and Tricks! Subscribe to our Newsletter.</div>
  <div class="btn-subscribe">Subscribe</div>
  <div class="btn-quote">Get a Free Quote!</div>
</div>
</body>
</html>
```